Wendrows Accountants and Tax Agents Practice

We need an update on our logo.
We require Letterhead, withcomp slips, and business cards for three partners
We currently have a logo and which is used on our letterheads but we need a much more professional and updated more modern version.
We are an Accounting Practice which needs upating. I will up load what we currently use and please use the all the wording and what another designer has proposed but need it to be different .
The colour scheme needs to be deep charcoal and a deep blue/green(065A7F) .

Target Market(s)

Individuals, companies, partnerships

Industry/Entity Type

Accounting

Font styles to use
Other font styles liked:
• ITC Avant Garde Gothic.

Colors
0393ce

Requirements
Must have
• Please follow the letter head upload the colour code and the colour charcoal.
• I would like the word Wendrows in bold Accountants (not bold) the font to be ITC Avant Garde Gothic.
• The business cards for all three partners need to have two sides the solid colour on one side with the name Wendrows Accountants. The other side with the name and details ( below details for each partner) Dorian Fellbracke FCPA, Gerald Trumbleton FCPA
• Martin Osgood (Blue/green) the T, F, E, W ( blue green) the rest in charcoal with white background
• FCPA
• 2718 Park Road Malvern VIC 3144
• T +61 3 94827713
• F + 61 9482 7159
• E martin@wendrows-example.com.au
• W wendrowsaccountants-example.com.au
• the letter faded letter G on the white side of the card in the top RH corner
Nice to have
• the letter G on the white side of the business card in shades of charcoal very faint
• Instead of E: for email using symbols for the details eg:✉

```html
<!DOCTYPE html>
<html lang="en">
<head>
<meta charset="utf-8">
<title>Wendrows Accountants – Business Card</title>
<link rel="stylesheet" href="https://fonts.googleapis.com/css2?family=Lato:ital,wght@0,300;0,400;0,700;0,900;1,400&display=swap">
<style>
  :root {
    --backdrop: #e9ebee;
    --card-white: #ffffff;
    --facet-grey: #eceef1;
    --facet-grey-dark: #e2e4e8;
    --brand-blue: #1f5fa8;
    --panel-blue-light: #3a86c6;
    --panel-blue-mid: #2c6db0;
    --panel-navy: #1b4a94;
    --panel-navy-deep: #123a7c;
    --stripe-blue: #3e93cf;
    --logo-faint: #5c88c6;
    --text-white: #ffffff;
    --rule-blue: #5fa3d8;
    --icon-box: #1f5fa8;
  }
  * { box-sizing: border-box; margin: 0; padding: 0; }
  html, body {
    width: 1200px; height: 1063px; overflow: hidden;
    background: var(--backdrop);
    font-family: "Lato", Arial, sans-serif;
  }
  .canvas { position: relative; width: 1200px; height: 1063px; }

  .card {
    position: absolute; left: 220px; width: 760px; height: 464px;
    overflow: hidden; box-shadow: 0 6px 18px rgba(0,0,0,.12);
  }
  .card-front { top: 50px; background: var(--card-white); }
  .card-back  { top: 550px; }
  .card svg.card-shapes { position: absolute; inset: 0; width: 100%; height: 100%; }

  .front-logo {
    position: absolute; left: 0; right: 0; top: 138px;
    text-align: center; color: var(--brand-blue);
    font-weight: 700; line-height: 1;
  }
  .front-logo .logo-name { display: block; font-size: 96px; letter-spacing: -1px; }
  .front-logo .logo-line { display: block; font-size: 62px; margin-top: 8px; }

  .back-logo {
    position: absolute; left: 470px; top: 52px; width: 270px;
    color: var(--logo-faint); font-weight: 700; line-height: 1;
  }
  .back-logo .logo-name { display: block; font-size: 50px; }
  .back-logo .logo-line { display: block; font-size: 32px; margin-top: 4px; }

  .details { position: absolute; left: 40px; top: 40px; width: 380px; color: var(--text-white); }
  .partner-name { font-size: 27px; font-weight: 900; letter-spacing: .3px; }
  .partner-title { font-size: 20px; font-weight: 300; margin-top: 4px; }
  .contact-group { display: flex; align-items: flex-start; gap: 16px; margin-top: 22px; }
  .icon-box {
    width: 36px; height: 36px; background: var(--icon-box);
    display: flex; align-items: center; justify-content: center; flex: none;
  }
  .icon-box svg { width: 22px; height: 22px; }
  .contact-lines { font-size: 17px; font-weight: 300; line-height: 1.4; white-space: nowrap; }
  .rule { height: 1px; background: var(--rule-blue); margin-top: 16px; width: 360px; }
  .address { font-size: 18px; font-weight: 400; margin-top: 18px; white-space: nowrap; }
</style>
</head>
<body>
<main class="canvas">

  <section class="card card-front" aria-label="Business card front">
    <svg class="card-shapes" viewBox="0 0 760 464" preserveAspectRatio="none" aria-hidden="true">
      <polygon points="0,0 120,0 0,130" fill="var(--facet-grey)"/>
      <polygon points="0,464 0,300 90,464" fill="var(--facet-grey)"/>
      <polygon points="640,0 760,0 760,464 690,464 700,60" fill="var(--facet-grey)"/>
      <polygon points="700,60 760,0 760,200" fill="var(--facet-grey-dark)"/>
      <polygon points="560,464 690,464 700,360" fill="var(--facet-grey)"/>
    </svg>
    <div class="front-logo">
      <span class="logo-name">Wendrows</span>
      <span class="logo-line">Accountants</span>
    </div>
  </section>

  <section class="card card-back" aria-label="Business card back">
    <svg class="card-shapes" viewBox="0 0 760 464" preserveAspectRatio="none" aria-hidden="true">
      <defs>
        <linearGradient id="leftPanel" x1="0" y1="0" x2="1" y2="0">
          <stop offset="0" stop-color="var(--panel-blue-mid)"/>
          <stop offset="1" stop-color="var(--panel-blue-light)"/>
        </linearGradient>
        <linearGradient id="rightPanel" x1="0" y1="0" x2="1" y2="1">
          <stop offset="0" stop-color="var(--panel-navy)"/>
          <stop offset="1" stop-color="var(--panel-navy-deep)"/>
        </linearGradient>
      </defs>
      <rect x="0" y="0" width="760" height="464" fill="url(#leftPanel)"/>
      <polygon points="330,464 430,250 430,464" fill="var(--stripe-blue)"/>
      <rect x="430" y="0" width="330" height="464" fill="url(#rightPanel)"/>
    </svg>

    <div class="back-logo">
      <span class="logo-name">Wendrows</span>
      <span class="logo-line">Accountants</span>
    </div>

    <div class="details">
      <p class="partner-name">Dorian Fellbracke</p>
      <p class="partner-title">FCPA</p>

      <div class="contact-group">
        <span class="icon-box">
          <svg viewBox="0 0 24 24" aria-hidden="true"><path fill="#fff" d="M6.6 10.8a15.1 15.1 0 0 0 6.6 6.6l2.2-2.2a1 1 0 0 1 1-.25 11.4 11.4 0 0 0 3.6.57 1 1 0 0 1 1 1V20a1 1 0 0 1-1 1A17 17 0 0 1 3 4a1 1 0 0 1 1-1h3.5a1 1 0 0 1 1 1c0 1.25.2 2.45.57 3.57a1 1 0 0 1-.25 1z"/></svg>
        </span>
        <p class="contact-lines">+61 3 94827713<br>+ 61 9482 7159</p>
      </div>
      <div class="rule"></div>

      <div class="contact-group">
        <span class="icon-box">
          <svg viewBox="0 0 24 24" aria-hidden="true" fill="none" stroke="#fff" stroke-width="1.6"><circle cx="12" cy="12" r="9"/><ellipse cx="12" cy="12" rx="4" ry="9"/><path d="M3 12h18M5 7h14M5 17h14"/></svg>
        </span>
        <p class="contact-lines">dorian@wendrows-example.com.au<br>www.wendrowsaccountants-example.com.au</p>
      </div>
      <div class="rule"></div>

      <p class="address">2718 Park Road Fernvale QLD 4999</p>
      <div class="rule"></div>
    </div>
  </section>

</main>
</body>
</html>
```